Schlichtes Design für Malerbetrieb
Zielgruppe
Wir sind ein mittelgroßer Malerbetrieb in München mit umfangreichem Leistungsspektrum.
Unsere Hauptleistungen sind: Fassadenrenovierung, Altbausanierung, Betoninstandsetzung, Balkonabdichtung (kein Neubau!).
Unsere Zielgruppen sind: Hausverwaltungen, Firmen und Privatpersonen.
Unsere Kunden schätzen: Konstruktive Organisation und Planung im Vorfeld, Zuverlässigkeit, saubere Arbeitsweise, dauerhafte Balkonabdichtungen.
Aufgabenstellung
Wir möchten eine langlebige, stilvolle, minimalistische Homepage.
Wir möchten von der bestehenden Homepage nur die Schriftart für unseren Firmennamen (Century Gothic) und wenn möglich (nicht zwingend), irgendwo das florale Muster einbauen. Corporate-Design haben wir nicht.
Farbtöne: Firmennamen Orange (hellorange bis erdiges Orange möglich, da sind wir nicht fixiert) , einen dunklen Hintergrundfarbton (Petrol-Blaugrau ?) mit gelbem (neon bis senfgelb) Akzent (Linien), Blumenmuster weiß, grau.
Dies sind nur unsere Ideen. Wir sind aber auch absolut offen für eure Profi-Ideen.
Wir möchten uns von den unzähligen langweiligen 'Pinselseiten mit veralteten Bilder' unserer Kollegen interessant und mit Stil abheben.
Eher nach dem Motto 'weniger ist mehr'.
Einen positiven, sympathischen Eindruck geben und unsere Leistungen in den Vordergrund bringen.
Da wir viele Stammkunden haben, betreiben wir kein Social-Media und möchten dies vorerst auch nicht tun.
Die Seite wird in den nächsten Jahren nicht verändert, höchstens die Bilder aktualisiert.
Die Texte haben wir alle selbst entworfen und möchten wir so übernehmen.
Die Galerien sollen unkompliziert anzuschauen sein.
Uns gefällt die Struktur und Schlichtheit von https://vormtakel.nl/ oder Tessuri.de gut und wir mögen Vintage-Grafiken gerne.
Einerseits darf die Seite geradlinig, andererseits aber auch rund und floral wirken.

```html
<!DOCTYPE html>
<html lang="de">
<head>
<meta charset="utf-8">
<title>brolkent Malerarbeiten</title>
<link href="https://fonts.googleapis.com/css2?family=Oswald:wght@300&family=Questrial&display=swap" rel="stylesheet">
<style>
  :root {
    --ink: #3a3a3c;
    --white: #ffffff;
    --petrol-light: #35606b;
    --petrol: #27434d;
    --petrol-dark: #1c2f37;
    --orange: #e98d37;
    --mustard: #d9b23a;
  }
  * { margin: 0; padding: 0; box-sizing: border-box; }
  html, body { width: 1200px; height: 900px; overflow: hidden; background: var(--white); }
  body { position: relative; font-family: "Oswald", sans-serif; color: var(--ink); }

  .main-nav {
    position: absolute; top: 58px; left: 30px; right: 23px;
    display: flex; justify-content: space-between;
  }
  .main-nav a, .footer-nav a {
    font-weight: 300; font-size: 21px; letter-spacing: 1.4px; line-height: 1.3;
    color: var(--ink); text-decoration: none; text-transform: uppercase;
  }

  .hero {
    position: absolute; top: 123px; left: 0; width: 1200px; height: 715px; overflow: hidden;
  }
  .hero-art {
    position: absolute; inset: 0;
    background: linear-gradient(125deg, var(--petrol-light) 0%, var(--petrol) 50%, var(--petrol-dark) 100%);
  }

  .brand {
    position: absolute; left: 0; right: 0; top: 342px;
    text-align: center;
  }
  .brand-name {
    font-family: "Questrial", sans-serif; font-size: 104px; line-height: 1;
    color: var(--orange); letter-spacing: 1px;
  }
  .brand-tagline {
    margin-top: 20px; margin-left: 12px;
    font-family: "Questrial", sans-serif; font-size: 25px;
    letter-spacing: 7px; color: var(--mustard);
  }

  .footer-nav {
    position: absolute; top: 855px; right: 23px;
    display: flex; gap: 16px;
  }
</style>
</head>
<body>
  <nav class="main-nav">
    <a href="#">Malerarbeiten</a>
    <a href="#">Betoninstandsetzung</a>
    <a href="#">Balkonabdichtung</a>
    <a href="#">Farbgestaltung</a>
    <a href="#">Wärmedämmung</a>
    <a href="#">Ausbildung</a>
    <a href="#">Portrait</a>
  </nav>

  <section class="hero">
    <div class="hero-art" role="img" aria-label="Grafische Farbflächen-Komposition mit Foto einer Farbrolle an der Wand"></div>
    <div class="brand">
      <div class="brand-name">brolkent</div>
      <div class="brand-tagline">MALERARBEITEN</div>
    </div>
  </section>

  <nav class="footer-nav">
    <a href="#">Kontakt</a>
    <a href="#">Impressum</a>
    <a href="#">Datenschutz</a>
  </nav>
</body>
</html>
```